PowerPoint Template Design for Management Consultancy

I need a PPT template for a new management consulting company. I want a modern look that uses dark blues and greys for divider slides, white content slides and a creative use of the logo in the slides. The supplied images are used on the website so I'd like to incorporate these into the theme

Target Market(s)

Management Consulting

Industry/Entity Type

Consulting

Font styles to use
Sans Serif

Colors
3277b5

Requirements
Must have
• Options for title slide, divider slides, content slides using the logo provided
Plain white content slides with creative use of logo
Color theme uses dark blues and greys
Nice to have
• Light and dark theme

```html
<!DOCTYPE html>
<html lang="en">
<head>
<meta charset="utf-8">
<title>Norvale Consulting – Master Slide Presentation</title>
<link href="https://fonts.googleapis.com/css2?family=Open+Sans:wght@400;600;700;800&display=swap" rel="stylesheet">
<style>
:root{
  --navy:#2d4470;
  --navy-deep:#23375d;
  --accent:#3277b5;
  --grey:#9a9ea4;
  --grey-light:#d9dce0;
  --ink:#2b3340;
  --muted:#8a9099;
  --paper:#ffffff;
  --stage:#eef0f3;
}
*{box-sizing:border-box;margin:0;padding:0}
html,body{width:1200px;height:4008px;overflow:hidden;background:var(--paper);font-family:"Open Sans",Arial,sans-serif;color:var(--ink)}
.canvas{position:relative;width:1200px;height:4008px}
.stage{position:absolute;left:0;top:0;width:1200px;height:1190px;background:var(--stage)}
.slide{position:absolute;background:var(--paper);overflow:hidden;font-size:10px;box-shadow:0 1px 4px rgba(30,45,70,.18)}
.slide::after{content:"";position:absolute;left:0;right:0;bottom:0;height:3px;background:linear-gradient(90deg,var(--navy) 70%,var(--grey) 70%)}
.slide.dark{background:var(--navy);color:#fff}
.slide.dark::after{background:linear-gradient(90deg,#fff 70%,var(--grey) 70%);opacity:.6}
.slide.greyed{background:var(--grey);color:#fff}
.abs{position:absolute}
.s-title{position:absolute;left:14px;top:12px;font-size:13px;font-weight:700;color:var(--navy);line-height:1.2}
.dark .s-title,.greyed .s-title{color:#fff}
.brand{font-weight:700;letter-spacing:.06em;color:var(--navy);line-height:1}
.slide>.brand.corner{position:absolute;right:14px;top:13px;font-size:10px}
.dark .brand,.greyed .brand{color:#fff}
.sub-brand{display:block;font-size:.38em;letter-spacing:.35em;font-weight:600;margin-top:.3em}
.foot{position:absolute;left:16px;bottom:8px;font-size:4.5px;letter-spacing:.15em;color:var(--muted)}
.page{position:absolute;right:16px;bottom:8px;font-size:4.5px;letter-spacing:.15em;color:var(--muted)}
.dark .foot,.dark .page,.greyed .foot,.greyed .page{color:#dfe4ee}
.txt{font-size:4.8px;line-height:1.5;color:var(--muted)}
.dark .txt,.greyed .txt{color:#dfe6f2}
.lbl{font-size:5.5px;font-weight:700;color:var(--ink)}
.dark .lbl{color:#fff}
.photo{position:absolute;background:linear-gradient(180deg,#f0c27a 0%,#c98a52 45%,#39465f 100%)}
.photo.cool{background:linear-gradient(160deg,#dfe3ea 0%,#a9b3c3 55%,#3c4a62 100%)}
.photo.desk{background:linear-gradient(150deg,#f4f5f7 0%,#c9cdd3 60%,#7b818a 100%)}
.photo.warm{background:linear-gradient(180deg,#f6d9a8 0%,#d5a56e 40%,#2e3b52 100%)}
.btn{display:inline-block;background:var(--navy);color:#fff;font-size:4px;font-weight:700;letter-spacing:.15em;padding:2px 7px;border-radius:10px}
.grid{position:absolute;left:16px;top:1222px;display:grid;grid-template-columns:repeat(3,375px);grid-auto-rows:212px;column-gap:20px;row-gap:20.3px}
.grid .slide{position:relative}
.watermark{position:absolute;font-weight:700;letter-spacing:.08em;color:var(--grey-light);line-height:1}
.dark .watermark{color:rgba(255,255,255,.18)}
.row{display:flex;gap:10px}
.num-badge{display:inline-flex;flex:none;align-items:center;justify-content:center;width:10px;height:10px;border-radius:50%;background:var(--navy);color:#fff;font-size:6px;font-weight:700}
.ico{display:inline-flex;flex:none;align-items:center;justify-content:center;width:22px;height:22px;border-radius:50%;border:1.2px solid var(--navy);background:#fff}
.sub{position:absolute;left:14px;top:32px;font-size:4px;letter-spacing:.3em;color:var(--muted)}
</style>
</head>
<body>
<div class="canvas">

<section class="stage" aria-label="Template showcase">

  <article class="slide dark" style="left:220px;top:80px;width:760px;height:430px">
    <div class="photo cool" role="img" aria-label="Faded photo of a climber on a mountain ridge" style="left:45%;top:0;width:47%;height:100%;opacity:.25"></div>
    <div class="abs" style="right:0;top:0;width:8%;height:100%;background:var(--grey)"></div>
    <div class="brand abs" style="left:48px;top:56px;font-size:36px">NORVALE<span class="sub-brand">CONSULTING</span></div>
    <div class="abs" style="left:48px;top:160px;font-size:10px;color:#dfe6f2">Month 2021</div>
    <div class="abs" style="left:48px;top:178px;font-size:24px;font-weight:700;line-height:1.25">Norvale Master Slide<br>Presentation</div>
    <div class="abs" style="left:48px;top:248px;font-size:9px;letter-spacing:.35em">SUBTITLE GOES HERE</div>
    <div class="abs row" style="left:48px;bottom:36px;gap:6px">
      <span style="width:14px;height:14px;border:1px solid #fff;border-radius:50%"></span>
      <span style="width:14px;height:14px;border:1px solid #fff;border-radius:50%"></span>
      <span style="width:14px;height:14px;border:1px solid #fff;border-radius:50%"></span>
    </div>
  </article>

  <article class="slide" style="left:40px;top:580px;width:360px;height:203px">
    <div class="photo" role="img" aria-label="Photo of two hikers celebrating on a summit at sunset" style="left:8%;top:14%;width:84%;height:70%;border-radius:0 0 20px 0"></div>
    <div class="abs" style="left:40%;top:140px;color:#fff;font-size:7px;font-weight:700">add your Content here</div>
    <div class="brand corner" style="top:9px">NORVALE</div>
    <span class="page">PAGE | 15</span>
  </article>

  <article class="slide" style="left:420px;top:580px;width:360px;height:203px">
    <h3 class="s-title">Timeline</h3><div class="brand corner">NORVALE</div>
    <svg class="abs" style="left:5%;top:30%;width:90%;height:45%" viewBox="0 0 300 80">
      <line x1="10" y1="40" x2="260" y2="40" stroke="#9a9ea4" stroke-width="1.5"/>
      <g fill="#9a9ea4"><circle cx="60" cy="40" r="6"/><circle cx="100" cy="40" r="6"/><circle cx="140" cy="40" r="6"/></g>
      <g fill="#2b3340"><circle cx="180" cy="40" r="6"/><circle cx="220" cy="40" r="6"/></g>
      <circle cx="265" cy="40" r="14" fill="#2d4470"/><text x="265" y="43" font-size="8" fill="#fff" text-anchor="middle" font-weight="700">2021</text>
      <text x="10" y="32" font-size="9" font-weight="700" fill="#2b3340">Start</text><text x="250" y="18" font-size="9" font-weight="700" fill="#2d4470">Vision</text>
    </svg>
    <span class="foot">NORVALE CONSULTING | 2021</span><span class="page">PAGE | 7</span>
  </article>

  <article class="slide" style="left:800px;top:580px;width:360px;height:203px">
    <div class="brand abs" style="left:50%;top:50%;transform:translate(-50%,-50%);font-size:25px;text-align:center">NORVALE<span class="sub-brand">CONSULTING</span></div>
  </article>

  <article class="slide" style="left:40px;top:850px;width:360px;height:203px">
    <div class="brand abs" style="left:14px;top:10px;font-size:10px">NORVALE</div>
    <div class="abs" style="left:14px;top:42px;font-size:11px;font-weight:700;color:var(--navy);line-height:1.2">Mission<br>Statement</div>
    <p class="txt abs" style="left:14px;top:82px;width:40%">Share the core purpose of the firm in a few clear lines that guide every client project.</p>
    <div class="photo warm" role="img" aria-label="Photo of climbers silhouetted on a rocky peak" style="left:55%;top:0;width:45%;height:100%"></div>
  </article>

  <article class="slide" style="left:420px;top:850px;width:360px;height:203px">
    <h3 class="s-title">Infographic Diagrams</h3>
    <svg class="abs" style="left:8%;top:25%;width:55%;height:65%" viewBox="0 0 200 120">
      <circle cx="55" cy="60" r="34" fill="none" stroke="#d9dce0" stroke-width="1.5"/>
      <text x="55" y="66" text-anchor="middle" font-size="20" font-weight="700" fill="#2d4470">N</text>
      <g fill="#2d4470"><circle cx="105" cy="20" r="9"/><circle cx="125" cy="45" r="9" fill="#9a9ea4"/><circle cx="125" cy="75" r="9" fill="#9a9ea4"/><circle cx="105" cy="100" r="9"/></g>
    </svg>
    <p class="txt abs" style="left:65%;top:34%;width:30%">Add a short note about each stage of this diagram here.</p>
  </article>

  <article class="slide" style="left:800px;top:850px;width:360px;height:203px">
    <div class="brand abs" style="left:50%;top:50%;transform:translate(-50%,-50%);font-size:22px;text-align:center">NORVALE<span class="sub-brand">TEMPLATE</span></div>
  </article>
</section>

<main class="grid">

  <!-- Row 1 -->
  <article class="slide">
    <div class="brand abs" style="left:50%;top:50%;transform:translate(-50%,-50%);font-size:26px;text-align:center">NORVALE<span class="sub-brand">CONSULTING</span></div>
  </article>

  <article class="slide">
    <div class="brand abs" style="left:38px;top:86px;font-size:22px;text-align:center">NORVALE<span class="sub-brand">CONSULTING</span></div>
    <div class="abs" style="left:190px;top:0;width:1px;height:100%;background:var(--grey-light)"></div>
    <div class="abs" style="left:200px;top:16px">
      <div style="font-size:12px;font-weight:800;color:var(--navy)">NORVALE CONSULTING</div>
      <div style="font-size:11px;font-weight:600;color:var(--grey)">TEMPLATE</div>
      <div style="font-size:4.5px;letter-spacing:.3em;color:var(--muted);margin-top:10px">SUBTITLE GOES HERE</div>
      <div style="font-size:4.5px;color:var(--muted);margin-top:14px">Month 2021</div>
    </div>
    <div class="abs" style="left:212px;bottom:22px;border:1px solid var(--navy);border-radius:10px;font-size:4.2px;padding:2px 9px;letter-spacing:.15em;color:var(--navy)">PRESENTER NAME</div>
  </article>

  <article class="slide dark">
    <div class="photo cool" role="img" aria-label="Faded photo of a climber on a mountain ridge" style="left:40%;top:0;width:52%;height:100%;opacity:.22"></div>
    <div class="abs" style="right:0;top:0;width:8%;height:100%;background:var(--grey)"></div>
    <div class="brand abs" style="left:16px;top:18px;font-size:18px">NORVALE<span class="sub-brand">CONSULTING</span></div>
    <div class="abs" style="left:16px;top:100px;font-size:4.5px">Month 2021</div>
    <div class="abs" style="left:16px;top:110px;font-size:11px;font-weight:700;line-height:1.3">Norvale Master Slide<br>Presentation</div>
    <div class="abs" style="left:16px;top:146px;font-size:4.2px;letter-spacing:.3em">SUBTITLE GOES HERE</div>
    <div class="abs row" style="left:16px;top:168px;gap:3px">
      <span style="width:7px;height:7px;border:1px solid #fff;border-radius:50%"></span>
      <span style="width:7px;height:7px;border:1px solid #fff;border-radius:50%"></span>
      <span style="width:7px;height:7px;border:1px solid #fff;border-radius:50%"></span>
    </div>
  </article>

  <!-- Row 2 -->
  <article class="slide">
    <h3 class="s-title">Agenda</h3>
    <div class="watermark" style="left:26px;top:94px;font-size:24px">NORVALE</div>
    <ol class="abs" style="left:57%;top:24px;list-style:none;width:38%">
      <li class="row" style="align-items:center;border-bottom:1px solid var(--grey-light);padding:4.5px 0"><b style="font-size:8px;color:var(--navy)">01</b><span class="txt">Introduction</span></li>
      <li class="row" style="align-items:center;border-bottom:1px solid var(--grey-light);padding:4.5px 0"><b style="font-size:8px;color:var(--navy)">02</b><span class="txt">About Us</span></li>
      <li class="row" style="align-items:center;border-bottom:1px solid var(--grey-light);padding:4.5px 0"><b style="font-size:8px;color:var(--navy)">03</b><span class="txt">Welcome Message</span></li>
      <li class="row" style="align-items:center;border-bottom:1px solid var(--grey-light);padding:4.5px 0"><b style="font-size:8px;color:var(--navy)">04</b><span class="txt">Our Services</span></li>
      <li class="row" style="align-items:center;border-bottom:1px solid var(--grey-light);padding:4.5px 0"><b style="font-size:8px;color:var(--navy)">05</b><span class="txt">Our Team</span></li>
      <li class="row" style="align-items:center;padding:4.5px 0"><b style="font-size:8px;color:var(--navy)">06</b><span class="txt">Contact Us</span></li>
    </ol>
    <span class="foot">NORVALE CONSULTING | 2021</span><span class="page">PAGE | 4</span>
  </article>

  <article class="slide">
    <h3 class="s-title">Table Of Content</h3><div class="brand corner">NORVALE</div>
    <div class="abs" style="left:16px;top:36px;right:16px;display:grid;grid-template-columns:1fr 1fr;row-gap:9px;column-gap:14px">
      <div class="row"><span style="font-size:20px;color:var(--grey);line-height:1">1</span><div><div class="lbl">Content here</div><p class="txt">Add a short line about this topic here.</p></div></div>
      <div class="row"><span style="font-size:20px;color:var(--grey);line-height:1">4</span><div><div class="lbl">Content here</div><p class="txt">Add a short line about this topic here.</p></div></div>
      <div class="row"><span style="font-size:20px;color:var(--grey);line-height:1">2</span><div><div class="lbl">Content here</div><p class="txt">Add a short line about this topic here.</p></div></div>
      <div class="row"><span style="font-size:20px;color:var(--grey);line-height:1">5</span><div><div class="lbl">Content here</div><p class="txt">Add a short line about this topic here.</p></div></div>
      <div class="row"><span style="font-size:20px;color:var(--grey);line-height:1">3</span><div><div class="lbl">Content here</div><p class="txt">Add a short line about this topic here.</p></div></div>
      <div class="row"><span style="font-size:20px;color:var(--grey);line-height:1">6</span><div><div class="lbl">Content here</div><p class="txt">Add a short line about this topic here.</p></div></div>
    </div>
    <span class="foot">NORVALE CONSULTING | 2021</span><span class="page">PAGE | 5</span>
  </article>

  <article class="slide">
    <h3 class="s-title">Welcome Message</h3><div class="brand corner">NORVALE</div>
    <div class="abs" style="left:22px;top:80px;width:40px;height:40px;border:1.5px solid var(--navy);border-radius:50%;display:flex;align-items:center;justify-content:center;font-size:20px;font-weight:800;color:var(--navy);line-height:1">&rdquo;</div>
    <div class="abs" style="left:78px;top:76px;width:1px;height:48px;background:var(--grey-light)"></div>
    <p class="txt abs" style="left:92px;top:80px;width:260px">You can simply impress your audience and add a unique design to your presentation. Easy to change colors, photos and text. A clean modern layout that is beautifully designed for every message.</p>
    <div class="abs" style="right:24px;top:124px;font-size:4.5px;color:var(--muted)">- Mara Ellis CEO</div>
    <span class="foot">NORVALE CONSULTING | 2021</span><span class="page">PAGE | 6</span>
  </article>

  <!-- Row 3 -->
  <article class="slide">
    <h3 class="s-title">Timeline</h3><div class="brand corner">NORVALE</div>
    <svg class="abs" style="left:4%;top:20%;width:92%;height:65%" viewBox="0 0 340 140">
      <line x1="20" y1="70" x2="290" y2="70" stroke="#9a9ea4" stroke-width="1.2"/>
      <g fill="#9a9ea4"><circle cx="70" cy="70" r="6"/><circle cx="110" cy="70" r="6"/><circle cx="150" cy="70" r="6"/></g>
      <g fill="#2b3340"><circle cx="190" cy="70" r="6"/><circle cx="230" cy="70" r="6"/><circle cx="265" cy="70" r="6"/></g>
      <circle cx="310" cy="70" r="15" fill="#2d4470"/><text x="310" y="73" text-anchor="middle" font-size="7" fill="#fff" font-weight="700">2021</text>
      <text x="10" y="64" font-size="9" font-weight="700" fill="#2b3340">Start</text><text x="10" y="76" font-size="6" fill="#8a9099">Contents</text>
      <text x="295" y="44" font-size="9" font-weight="700" fill="#2d4470">Vision</text>
      <g font-size="5" fill="#8a9099" text-anchor="middle"><text x="70" y="58">2013</text><text x="110" y="86">2014</text><text x="150" y="58">2015</text><text x="190" y="86">2016</text><text x="230" y="58">2017</text><text x="265" y="86">2020</text></g>
      <g font-size="5" fill="#8a9099" text-anchor="middle"><text x="110" y="30">Content</text><text x="190" y="30">Content</text><text x="265" y="30">Content</text><text x="70" y="110">Content</text><text x="150" y="110">Content</text><text x="230" y="110">Content</text></g>
    </svg>
    <span class="foot">NORVALE CONSULTING | 2021</span><span class="page">PAGE | 7</span>
  </article>

  <article class="slide">
    <h3 class="s-title">Your Title Here - One Column</h3><div class="brand corner">NORVALE</div>
    <div class="abs" style="left:18px;top:46px;width:38%"><div class="lbl">Content Here</div><p class="txt" style="margin-top:8px">You can simply impress your audience and add a unique design to your presentation. Easy to change colors, photos and text. Get a modern layout that is beautifully designed and simple to edit for every message you share.</p></div>
    <div class="watermark" style="right:30px;top:94px;font-size:20px">NORVALE</div>
    <span class="foot">NORVALE CONSULTING | 2021</span><span class="page">PAGE | 8</span>
  </article>

  <article class="slide dark">
    <h3 class="s-title">Your Title Here - One Column</h3><div class="brand corner">NORVALE</div>
    <div class="abs" style="left:18px;top:46px;width:38%"><div class="lbl">Content Here</div><p class="txt" style="margin-top:8px">You can simply impress your audience and add a unique design to your presentation. Easy to change colors, photos and text. Get a modern layout that is beautifully designed and simple to edit for every message you share.</p></div>
    <div class="watermark" style="right:30px;top:94px;font-size:20px">NORVALE</div>
    <span class="foot">NORVALE CONSULTING | 2021</span><span class="page">PAGE | 9</span>
  </article>

  <!-- Row 4 -->
  <article class="slide">
    <h3 class="s-title">Your Title Here</h3><div class="brand corner">NORVALE</div>
    <div class="abs" style="left:18px;top:40px;display:flex;flex-direction:column;gap:10px;width:42%">
      <div class="row" style="align-items:center"><span class="ico" style="background:var(--navy)"></span><div><div class="lbl">Content Here</div><p class="txt">Add a short line about this point.</p></div></div>
      <div class="row" style="align-items:center"><span class="ico" style="background:var(--grey-light);border-color:var(--grey)"></span><div><div class="lbl">Content Here</div><p class="txt">Add a short line about this point.</p></div></div>
      <div class="row" style="align-items:center"><span class="ico" style="background:var(--ink);border-color:var(--ink)"></span><div><div class="lbl">Content Here</div><p class="txt">Add a short line about this point.</p></div></div>
    </div>
    <div class="abs" style="left:52%;top:40px;width:42%"><div class="lbl">Content Here</div><p class="txt" style="margin:6px 0 10px">You can simply impress your audience and add a unique design to your presentation. Easy to change colors, photos and text in a few clicks.</p><span class="btn">LEARN MORE</span></div>
    <span class="foot">NORVALE CONSULTING | 2021</span><span class="page">PAGE | 10</span>
  </article>

  <article class="slide">
    <h3 class="s-title">Your Title Here - Two Column</h3><div class="brand corner">NORVALE</div>
    <div class="sub">SUBTITLE GOES HERE</div>
    <div class="abs row" style="left:18px;right:18px;top:52px;gap:20px">
      <div style="flex:1"><div class="lbl">Content Here</div><p class="txt" style="margin-top:6px">You can simply impress your audience and add a unique design to your presentation. Easy to change colors, photos and text. A modern layout that is beautifully designed.</p></div>
      <div style="flex:1"><div class="lbl">Content Here</div><p class="txt" style="margin-top:6px">You can simply impress your audience and add a unique design to your presentation. Easy to change colors, photos and text. A modern layout that is beautifully designed.</p></div>
    </div>
    <span class="foot">NORVALE CONSULTING | 2021</span><span class="page">PAGE | 11</span>
  </article>

  <article class="slide">
    <h3 class="s-title">Your Title Here - Three Column</h3><div class="brand corner">NORVALE</div>
    <div class="sub">SUBTITLE GOES HERE</div>
    <div class="abs row" style="left:18px;right:18px;top:52px;gap:14px">
      <div style="flex:1"><div class="lbl">Content Here</div><p class="txt" style="margin-top:6px">You can simply impress your audience and add a unique design. Easy to change colors, photos and text in a clean layout.</p></div>
      <div style="flex:1"><div class="lbl">Content Here</div><p class="txt" style="margin-top:6px">You can simply impress your audience and add a unique design. Easy to change colors, photos and text in a clean layout.</p></div>
      <div style="flex:1"><div class="lbl">Content Here</div><p class="txt" style="margin-top:6px">You can simply impress your audience and add a unique design. Easy to change colors, photos and text in a clean layout.</p></div>
    </div>
    <span class="foot">NORVALE CONSULTING | 2021</span><span class="page">PAGE | 12</span>
  </article>

  <!-- Row 5 -->
  <article class="slide">
    <h3 class="s-title">Your Title Here</h3><div class="brand corner">NORVALE</div>
    <div class="abs" style="left:18px;top:50px;width:36%"><div class="lbl" style="text-align:right">Content Here</div><p class="txt" style="margin-top:6px">You can simply impress your audience and add a unique design to your presentation. Easy to change colors, photos and text for every message.</p></div>
    <div class="photo" role="img" aria-label="Photo of two hikers celebrating on a summit at sunset" style="left:48%;top:34px;width:46%;height:120px;border-radius:0 0 16px 0"></div>
    <div class="abs" style="left:60%;top:142px;font-size:5px;font-weight:700;color:#fff">add your Content here</div>
    <span class="foot">NORVALE CONSULTING | 2021</span><span class="page">PAGE | 13</span>
  </article>

  <article class="slide dark">
    <h3 class="s-title">Your Title Here</h3><div class="brand corner">NORVALE</div>
    <div class="abs" style="left:18px;top:42px;width:40%"><div class="lbl" style="text-align:right">Content Here</div><p class="txt" style="margin-top:6px">You can simply impress your audience and add a unique design to your presentation. Easy to change colors, photos and text. Get a modern layout that is beautifully designed for your firm.</p></div>
    <div class="photo desk" role="img" aria-label="Photo of a laptop on a white desk" style="left:48%;top:40px;width:46%;height:110px"></div>
    <span class="foot">NORVALE CONSULTING | 2021</span><span class="page">PAGE | 14</span>
  </article>

  <article class="slide">
    <h3 class="s-title">Bullets Points</h3><div class="brand corner">NORVALE</div>
    <div class="abs" style="left:18px;right:18px;top:38px;display:grid;grid-template-columns:1fr 1fr;row-gap:10px;column-gap:16px">
      <div class="row" style="align-items:center"><span class="num-badge">1</span><div><div class="lbl">Content Title here</div><p class="txt">Add a short line about this point.</p></div></div>
      <div class="row" style="align-items:center"><span class="num-badge">4</span><div><div class="lbl">Content Title here</div><p class="txt">Add a short line about this point.</p></div></div>
      <div class="row" style="align-items:center"><span class="num-badge">2</span><div><div class="lbl">Content Title here</div><p class="txt">Add a short line about this point.</p></div></div>
      <div class="row" style="align-items:center"><span class="num-badge">5</span><div><div class="lbl">Content Title here</div><p class="txt">Add a short line about this point.</p></div></div>
      <div class="row" style="align-items:center"><span class="num-badge">3</span><div><div class="lbl">Content Title here</div><p class="txt">Add a short line about this point.</p></div></div>
      <div class="row" style="align-items:center"><span class="num-badge">6</span><div><div class="lbl">Content Title here</div><p class="txt">Add a short line about this point.</p></div></div>
    </div>
    <span class="foot">NORVALE CONSULTING | 2021</span><span class="page">PAGE | 15</span>
  </article>

  <!-- Row 6 -->
  <article class="slide">
    <h3 class="s-title">Your Title Here</h3><div class="brand corner">NORVALE</div>
    <div class="abs" style="left:18px;right:18px;top:38px;display:flex;flex-direction:column;gap:5px">
      <div class="row" style="border:1px solid var(--grey-light);padding:4px 6px;align-items:center"><span class="lbl" style="width:25%">Content here</span><p class="txt">Add a short line about this point for your audience and clients here.</p></div>
      <div class="row" style="border:1px solid var(--grey-light);padding:4px 6px;align-items:center"><span class="lbl" style="width:25%">Content here</span><p class="txt">Add a short line about this point for your audience and clients here.</p></div>
      <div class="row" style="border:1px solid var(--grey-light);padding:4px 6px;align-items:center"><span class="lbl" style="width:25%">Content here</span><p class="txt">Add a short line about this point for your audience and clients here.</p></div>
      <div class="row" style="border:1px solid var(--grey-light);padding:4px 6px;align-items:center"><span class="lbl" style="width:25%">Content here</span><p class="txt">Add a short line about this point for your audience and clients here.</p></div>
    </div>
    <span class="foot">NORVALE CONSULTING | 2021</span><span class="page">PAGE | 16</span>
  </article>

  <article class="slide">
    <h3 class="s-title">Infographic Diagrams</h3><div class="brand corner">NORVALE</div>
    <svg class="abs" style="left:5%;top:22%;width:48%;height:68%" viewBox="0 0 200 140">
      <circle cx="60" cy="70" r="40" fill="none" stroke="#d9dce0" stroke-width="1.5"/>
      <text x="60" y="72" text-anchor="middle" font-size="22" font-weight="700" fill="#2d4470">N</text>
      <text x="60" y="86" text-anchor="middle" font-size="5" fill="#8a9099">Add your note</text>
      <circle cx="118" cy="18" r="10" fill="#2d4470"/><circle cx="140" cy="52" r="10" fill="#9a9ea4"/><circle cx="140" cy="88" r="10" fill="#d9dce0"/><circle cx="118" cy="122" r="10" fill="#2b3340"/>
    </svg>
    <div class="abs" style="left:54%;top:42px;width:40%;display:flex;flex-direction:column;gap:7px">
      <div><div class="lbl">Content Title</div><p class="txt">Add a short line about this stage.</p></div>
      <div><div class="lbl">Content Title</div><p class="txt">Add a short line about this stage.</p></div>
      <div><div class="lbl">Content Title</div><p class="txt">Add a short line about this stage.</p></div>
      <div><div class="lbl">Content Title</div><p class="txt">Add a short line about this stage.</p></div>
    </div>
    <span class="foot">NORVALE CONSULTING | 2021</span><span class="page">PAGE | 17</span>
  </article>

  <article class="slide">
    <h3 class="s-title">Pie Charts</h3><div class="brand corner">NORVALE</div>
    <p class="txt abs" style="left:12%;right:12%;top:36px;text-align:center">Add a short summary for these charts here. Easy to change colors, photos and text for your audience.</p>
    <svg class="abs" style="left:8%;top:40%;width:84%;height:34%" viewBox="0 0 300 70">
      <g transform="translate(50 35)"><circle r="26" fill="none" stroke="#eef0f3" stroke-width="8"/><circle r="26" fill="none" stroke="#2d4470" stroke-width="8" stroke-dasharray="111 163" transform="rotate(-90)"/><text y="5" text-anchor="middle" font-size="13" font-weight="700" fill="#2d4470">68%</text></g>
      <g transform="translate(150 35)"><circle r="26" fill="none" stroke="#eef0f3" stroke-width="8"/><circle r="26" fill="none" stroke="#9a9ea4" stroke-width="8" stroke-dasharray="57 163" transform="rotate(-90)"/><text y="5" text-anchor="middle" font-size="13" font-weight="700" fill="#9a9ea4">35%</text></g>
      <g transform="translate(250 35)"><circle r="26" fill="none" stroke="#eef0f3" stroke-width="8"/><circle r="26" fill="none" stroke="#d9dce0" stroke-width="8" stroke-dasharray="90 163" transform="rotate(-90)"/><text y="5" text-anchor="middle" font-size="13" font-weight="700" fill="#d9dce0">55%</text></g>
    </svg>
    <div class="abs row" style="left:8%;right:8%;top:160px;justify-content:space-around"><p class="txt" style="width:26%;text-align:center">Add a short note here.</p><p class="txt" style="width:26%;text-align:center">Add a short note here.</p><p class="txt" style="width:26%;text-align:center">Add a short note here.</p></div>
    <span class="foot">NORVALE CONSULTING | 2021</span><span class="page">PAGE | 18</span>
  </article>

  <!-- Row 7 -->
  <article class="slide">
    <h3 class="s-title">Bar Chart</h3><div class="brand corner">NORVALE</div>
    <p class="txt abs" style="left:36px;top:34px">Add a short summary for this chart in one line here.</p>
    <svg class="abs" style="left:5%;top:28%;width:90%;height:62%" viewBox="0 0 320 120">
      <g stroke="#eef0f3" stroke-width="1"><line x1="20" y1="10" x2="310" y2="10"/><line x1="20" y1="35" x2="310" y2="35"/><line x1="20" y1="60" x2="310" y2="60"/><line x1="20" y1="85" x2="310" y2="85"/><line x1="20" y1="110" x2="310" y2="110"/></g>
      <g fill="#d9dce0"><rect x="30" y="10" width="14" height="100"/><rect x="65" y="10" width="14" height="100"/><rect x="100" y="10" width="14" height="100"/><rect x="135" y="10" width="14" height="100"/><rect x="170" y="10" width="14" height="100"/><rect x="205" y="10" width="14" height="100"/><rect x="240" y="10" width="14" height="100"/><rect x="275" y="10" width="14" height="100"/></g>
      <g fill="#9a9ea4"><rect x="30" y="60" width="14" height="28"/><rect x="100" y="50" width="14" height="36"/><rect x="170" y="46" width="14" height="40"/><rect x="240" y="52" width="14" height="34"/></g>
      <g fill="#2d4470"><rect x="30" y="88" width="14" height="22"/><rect x="65" y="55" width="14" height="55"/><rect x="100" y="86" width="14" height="24"/><rect x="135" y="40" width="14" height="70"/><rect x="170" y="86" width="14" height="24"/><rect x="205" y="35" width="14" height="75"/><rect x="240" y="86" width="14" height="24"/><rect x="275" y="30" width="14" height="80"/></g>
      <g font-size="5" fill="#8a9099"><text x="2" y="12">100%</text><text x="6" y="37">75%</text><text x="6" y="62">50%</text><text x="6" y="87">25%</text><text x="10" y="112">0%</text></g>
      <g font-size="5" fill="#8a9099" text-anchor="middle"><text x="37" y="118">2012</text><text x="72" y="118">2013</text><text x="107" y="118">2014</text><text x="142" y="118">2015</text><text x="177" y="118">2016</text><text x="212" y="118">2017</text><text x="247" y="118">2018</text><text x="282" y="118">2019</text></g>
    </svg>
    <span class="foot">NORVALE CONSULTING | 2021</span><span class="page">PAGE | 19</span>
  </article>

  <article class="slide">
    <h3 class="s-title">Table Chart</h3><div class="brand corner">NORVALE</div>
    <svg class="abs" style="left:6%;top:25%;width:88%;height:65%" viewBox="0 0 320 130">
      <g fill="#2d4470"><rect x="40" y="0" width="80" height="8"/><rect x="130" y="0" width="80" height="8"/><rect x="220" y="0" width="80" height="8"/></g>
      <g font-size="5" fill="#fff" text-anchor="middle" font-weight="700"><text x="80" y="6">TEXT HERE</text><text x="170" y="6">TEXT HERE</text><text x="260" y="6">TEXT HERE</text></g>
      <g fill="#eef0f3"><rect x="40" y="14" width="260" height="18"/><rect x="40" y="58" width="260" height="18"/><rect x="40" y="102" width="260" height="18"/></g>
      <g stroke="#d9dce0"><line x1="125" y1="12" x2="125" y2="124"/><line x1="215" y1="12" x2="215" y2="124"/></g>
      <g fill="#2d4470"><circle cx="22" cy="23" r="6"/><circle cx="22" cy="45" r="6" fill="#9a9ea4"/><circle cx="22" cy="67" r="6"/><circle cx="22" cy="89" r="6" fill="#9a9ea4"/><circle cx="22" cy="111" r="6"/></g>
      <g font-size="5" fill="#8a9099" text-anchor="middle">
        <text x="80" y="25">Add Content Title</text><text x="170" y="25">Add Content Title</text><text x="260" y="25">Add Content Title</text>
        <text x="80" y="47">Modern Layout</text><text x="170" y="47">Modern Layout</text><text x="260" y="47">Modern Layout</text>
        <text x="80" y="69">Add Content Title</text><text x="170" y="69">Add Content Title</text><text x="260" y="69">Add Content Title</text>
        <text x="80" y="91">Modern Layout</text><text x="170" y="91">Modern Layout</text><text x="260" y="91">Modern Layout</text>
        <text x="80" y="113">Add Content Title</text><text x="170" y="113">Add Content Title</text><text x="260" y="113">Add Content Title</text>
      </g>
    </svg>
    <span class="foot">NORVALE CONSULTING | 2021</span><span class="page">PAGE | 20</span>
  </article>

  <article class="slide">
    <h3 class="s-title">Text with Graph</h3><div class="brand corner">NORVALE</div>
    <div class="abs" style="left:18px;top:46px;width:38%"><div class="lbl">Content Here</div><p class="txt" style="margin:6px 0 10px">You can simply impress your audience and add a unique design to your presentation. Easy to change colors, photos and text in any layout.</p><span class="btn">LEARN MORE</span></div>
    <svg class="abs" style="left:50%;top:22%;width:45%;height:66%" viewBox="0 0 160 110">
      <g stroke="#eef0f3"><line x1="10" y1="10" x2="155" y2="10"/><line x1="10" y1="35" x2="155" y2="35"/><line x1="10" y1="60" x2="155" y2="60"/><line x1="10" y1="85" x2="155" y2="85"/></g>
      <polyline points="15,60 40,20 65,55 90,80 115,60 150,45" fill="none" stroke="#2d4470" stroke-width="2"/>
      <polyline points="15,70 40,65 65,40 90,55 115,65 150,30" fill="none" stroke="#9a9ea4" stroke-width="1.5"/>
      <polyline points="15,80 40,75 65,70 90,60 115,50 150,40" fill="none" stroke="#2b3340" stroke-width="1" stroke-dasharray="3 2"/>
    </svg>
    <span class="foot">NORVALE CONSULTING | 2021</span><span class="page">PAGE | 21</span>
  </article>

  <!-- Row 8 -->
  <article class="slide dark">
    <div class="brand abs" style="left:16px;top:18px;font-size:18px">NORVALE<span class="sub-brand">CONSULTING</span></div>
    <div class="abs" style="left:16px;top:112px;font-size:12px;font-weight:700;border:1px solid #fff;padding:0 4px;line-height:1.4">01</div>
    <div class="abs" style="left:16px;top:138px;font-size:11px;font-weight:700">SECTION TITLE</div>
    <p class="txt abs" style="left:16px;top:158px;width:70%">Add a short note about this section of the talk here.</p>
  </article>

  <article class="slide greyed">
    <div class="brand abs" style="left:16px;top:18px;font-size:18px">NORVALE<span class="sub-brand">CONSULTING</span></div>
    <div class="abs" style="left:16px;top:112px;font-size:12px;font-weight:700;border:1px solid #fff;padding:0 4px;line-height:1.4">02</div>
    <div class="abs" style="left:16px;top:138px;font-size:11px;font-weight:700">SECTION TITLE</div>
    <p class="txt abs" style="left:16px;top:158px;width:70%">Add a short note about this section of the talk here.</p>
  </article>

  <article class="slide">
    <h3 class="s-title">Our Process</h3><div class="brand corner">NORVALE</div>
    <svg class="abs" style="left:4%;top:24%;width:92%;height:32%" viewBox="0 0 340 60">
      <g fill="#2d4470"><polygon points="0,10 58,10 70,30 58,50 0,50 12,30"/><polygon points="136,10 194,10 206,30 194,50 136,50 148,30"/><polygon points="272,10 330,10 340,30 330,50 272,50 284,30"/></g>
      <g fill="#9a9ea4"><polygon points="68,10 126,10 138,30 126,50 68,50 80,30"/><polygon points="204,10 262,10 274,30 262,50 204,50 216,30"/></g>
      <g font-size="6" fill="#fff" text-anchor="middle" font-weight="700"><text x="36" y="42">Step 01</text><text x="103" y="42">Step 02</text><text x="171" y="42">Step 03</text><text x="239" y="42">Step 04</text><text x="306" y="42">Step 05</text></g>
    </svg>
    <div class="abs row" style="left:16px;right:16px;top:122px;gap:6px">
      <div style="flex:1"><div class="lbl">Content Here</div><p class="txt">Add a short note on this step.</p></div>
      <div style="flex:1"><div class="lbl">Content Here</div><p class="txt">Add a short note on this step.</p></div>
      <div style="flex:1"><div class="lbl">Content Here</div><p class="txt">Add a short note on this step.</p></div>
      <div style="flex:1"><div class="lbl">Content Here</div><p class="txt">Add a short note on this step.</p></div>
      <div style="flex:1"><div class="lbl">Content Here</div><p class="txt">Add a short note on this step.</p></div>
    </div>
    <span class="foot">NORVALE CONSULTING | 2021</span><span class="page">PAGE | 24</span>
  </article>

  <!-- Row 9 -->
  <article class="slide">
    <h3 class="s-title">Our Process</h3><div class="brand corner">NORVALE</div>
    <div class="abs row" style="left:16px;right:16px;top:48px;gap:5px;text-align:center">
      <div style="flex:1"><span class="ico" style="background:var(--grey-light);border-color:var(--grey)"></span><div class="lbl" style="margin:6px 0 3px">LOREM IPSUM</div><p class="txt">Add a short note on this stage here.</p></div>
      <div style="flex:1"><span class="ico" style="background:var(--grey-light);border-color:var(--grey)"></span><div class="lbl" style="margin:6px 0 3px">LOREM IPSUM</div><p class="txt">Add a short note on this stage here.</p></div>
      <div style="flex:1"><span class="ico"></span><div class="lbl" style="margin:6px 0 3px">LOREM IPSUM</div><p class="txt">Add a short note on this stage here.</p></div>
      <div style="flex:1"><span class="ico" style="background:var(--grey-light);border-color:var(--grey)"></span><div class="lbl" style="margin:6px 0 3px">LOREM IPSUM</div><p class="txt">Add a short note on this stage here.</p></div>
      <div style="flex:1"><span class="ico"></span><div class="lbl" style="margin:6px 0 3px">LOREM IPSUM</div><p class="txt">Add a short note on this stage here.</p></div>
      <div style="flex:1"><span class="ico"></span><div class="lbl" style="margin:6px 0 3px">LOREM IPSUM</div><p class="txt">Add a short note on this stage here.</p></div>
    </div>
    <span class="foot">NORVALE CONSULTING | 2021</span><span class="page">PAGE | 25</span>
  </article>

  <article class="slide">
    <h3 class="s-title">Infographic Style</h3><div class="brand corner">NORVALE</div>
    <div class="abs" style="left:16px;top:40px;width:150px;height:128px;border:1.5px solid var(--navy);border-radius:6px"></div>
    <div class="abs" style="left:22px;top:34px;width:16px;height:16px;border-radius:50%;background:var(--navy);color:#fff;font-size:9px;font-weight:700;display:flex;align-items:center;justify-content:center">$</div>
    <div class="abs" style="left:30px;top:52px;font-size:40px;font-weight:800;color:var(--navy);line-height:1">08</div>
    <div class="abs" style="left:112px;top:88px;font-size:4.5px;background:var(--navy);color:#fff;padding:2px 6px">COST</div>
    <div class="abs" style="left:36px;top:104px;font-size:9px;font-weight:700;color:var(--navy)">Million</div>
    <p class="txt abs" style="left:26px;top:124px;width:130px;text-align:center">Add a short note on this figure.</p>
    <div class="abs" style="left:190px;top:40px;font-size:32px;font-weight:800;color:var(--grey);line-height:1">04</div>
    <div class="abs" style="left:244px;top:44px;font-size:4.5px;background:var(--grey);color:#fff;padding:2px 6px">SALES</div>
    <div class="abs" style="left:244px;top:58px;font-size:7px;font-weight:700;color:var(--grey)">Million</div>
    <p class="txt abs" style="left:290px;top:42px;width:70px">Add a short note on this figure.</p>
    <div class="abs" style="left:190px;top:104px;font-size:32px;font-weight:800;color:var(--grey-light);line-height:1">15</div>
    <div class="abs" style="left:244px;top:122px;font-size:4.5px;background:var(--grey-light);color:#fff;padding:2px 6px">PROFIT</div>
    <p class="txt abs" style="left:290px;top:108px;width:70px">Add a short note on this figure.</p>
    <span class="foot">NORVALE CONSULTING | 2021</span><span class="page">PAGE | 26</span>
  </article>

  <article class="slide">
    <h3 class="s-title">Our Structure</h3><div class="brand corner">NORVALE</div>
    <svg class="abs" style="left:5%;top:20%;width:38%;height:72%" viewBox="0 0 120 120">
      <circle cx="60" cy="60" r="45" fill="none" stroke="#2d4470" stroke-width="22" stroke-dasharray="141 283" transform="rotate(90 60 60)"/>
      <circle cx="60" cy="60" r="45" fill="none" stroke="#9a9ea4" stroke-width="22" stroke-dasharray="85 283" stroke-dashoffset="-141" transform="rotate(90 60 60)"/>
      <circle cx="60" cy="60" r="45" fill="none" stroke="#d9dce0" stroke-width="22" stroke-dasharray="57 283" stroke-dashoffset="-226" transform="rotate(90 60 60)"/>
      <circle cx="60" cy="60" r="26" fill="#fff" stroke="#2d4470" stroke-width="1.5"/>
      <text x="60" y="67" text-anchor="middle" font-size="20" font-weight="700" fill="#2d4470">N</text>
      <g font-size="7" font-weight="700" fill="#fff"><text x="12" y="62">50%</text><text x="92" y="40">30%</text><text x="86" y="94">20%</text></g>
    </svg>
    <div class="abs" style="left:52%;top:42px;width:42%;display:flex;flex-direction:column;gap:8px">
      <p class="txt" style="border-left:2px solid var(--navy);padding-left:6px">Add a short note on this part of the team here.</p>
      <p class="txt" style="border-left:2px solid var(--grey);padding-left:6px">Add a short note on this part of the team here.</p>
      <p class="txt" style="border-left:2px solid var(--grey-light);padding-left:6px">Add a short note on this part of the team here.</p>
      <p class="txt" style="border-left:2px solid var(--navy);padding-left:6px">Add a short note on this part of the team here.</p>
    </div>
    <span class="foot">NORVALE CONSULTING | 2021</span><span class="page">PAGE | 27</span>
  </article>

  <!-- Row 10 -->
  <article class="slide">
    <h3 class="s-title">Our Team</h3><div class="brand corner">NORVALE</div>
    <div class="abs row" style="left:16px;right:16px;top:36px;gap:8px;text-align:center">
      <div style="flex:1"><div class="photo desk" role="img" aria-label="Portrait photo of a team member" style="position:relative;height:74px"></div><div style="background:var(--navy);color:#fff;font-size:4.5px;padding:3px">Member Name</div><div class="lbl" style="margin-top:4px">POSITION</div><p class="txt">Add a short note on this role.</p></div>
      <div style="flex:1"><div class="photo desk" role="img" aria-label="Portrait photo of a team member" style="position:relative;height:74px"></div><div style="background:var(--navy);color:#fff;font-size:4.5px;padding:3px">Member Name</div><div class="lbl" style="margin-top:4px">POSITION</div><p class="txt">Add a short note on this role.</p></div>
      <div style="flex:1"><div class="photo desk" role="img" aria-label="Portrait photo of a team member" style="position:relative;height:74px"></div><div style="background:var(--navy);color:#fff;font-size:4.5px;padding:3px">Member Name</div><div class="lbl" style="margin-top:4px">POSITION</div><p class="txt">Add a short note on this role.</p></div>
      <div style="flex:1"><div class="photo desk" role="img" aria-label="Portrait photo of a team member" style="position:relative;height:74px"></div><div style="background:var(--navy);color:#fff;font-size:4.5px;padding:3px">Member Name</div><div class="lbl" style="margin-top:4px">POSITION</div><p class="txt">Add a short note on this role.</p></div>
    </div>
    <span class="foot">NORVALE CONSULTING | 2021</span><span class="page">PAGE | 28</span>
  </article>

  <article class="slide">
    <div class="brand abs" style="left:14px;top:12px;font-size:10px">NORVALE</div>
    <div class="abs" style="left:14px;top:46px;font-size:11px;font-weight:700;color:var(--navy);line-height:1.2">Mission<br>Statement</div>
    <div class="abs" style="left:146px;top:40px;font-size:22px;font-weight:800;color:var(--grey-light);line-height:1">&rdquo;</div>
    <p class="txt abs" style="left:14px;top:84px;width:160px">You can simply impress your audience and add a unique design to your presentation. Easy to change colors, photos and text. A modern layout that is beautifully designed for every client.</p>
    <div class="photo warm" role="img" aria-label="Photo of climbers silhouetted on a rocky peak above a misty valley" style="left:52%;top:0;width:48%;height:100%"></div>
    <span class="foot">NORVALE CONSULTING | 2021</span>
  </article>

  <article class="slide">
    <h3 class="s-title">Comparison</h3><div class="brand corner">NORVALE</div>
    <div class="abs" style="left:14px;top:38px;width:45%;height:136px;border:1px solid var(--grey-light);border-radius:6px;padding:6px 6px 6px 26px;display:flex;flex-direction:column;gap:5px">
      <p class="txt">1&nbsp; Add a short point for option one here.</p><p class="txt">2&nbsp; Add a short point for option one here.</p><p class="txt">3&nbsp; Add a short point for option one here.</p><p class="txt">4&nbsp; Add a short point for option one here.</p><p class="txt">5&nbsp; Add a short point for option one here.</p>
    </div>
    <div class="abs" style="left:10px;top:98px;width:14px;height:14px;background:var(--navy);color:#fff;font-size:8px;font-weight:700;display:flex;align-items:center;justify-content:center">A</div>
    <div class="abs" style="left:52%;top:38px;width:45%;height:136px;border:1px solid var(--grey-light);border-radius:6px;padding:6px 6px 6px 26px;display:flex;flex-direction:column;gap:5px">
      <p class="txt">1&nbsp; Add a short point for option two here.</p><p class="txt">2&nbsp; Add a short point for option two here.</p><p class="txt">3&nbsp; Add a short point for option two here.</p><p class="txt">4&nbsp; Add a short point for option two here.</p><p class="txt">5&nbsp; Add a short point for option two here.</p>
    </div>
    <div class="abs" style="left:191px;top:98px;width:14px;height:14px;background:var(--grey);color:#fff;font-size:8px;font-weight:700;display:flex;align-items:center;justify-content:center">B</div>
    <span class="foot">NORVALE CONSULTING | 2021</span><span class="page">PAGE | 30</span>
  </article>

  <!-- Row 11 -->
  <article class="slide">
    <div class="photo" role="img" aria-label="Photo of a hand writing with a pen on a notebook, tinted navy" style="left:0;top:0;width:50%;height:100%;background:linear-gradient(160deg,#4d6a9a 0%,var(--navy) 70%)"></div>
    <div class="abs" style="left:60px;top:16px;font-size:13px;font-weight:700;color:#fff">Case Study</div>
    <p class="txt abs" style="left:20px;top:140px;width:140px;color:#fff">Lorem ipsum is simply dummy text of the printing and typesetting industry.</p>
    <div class="abs" style="left:132px;top:170px;font-size:4.5px;color:#fff">Name Here</div>
    <div class="abs" style="left:55%;top:24px;width:40%;display:flex;flex-direction:column;gap:12px">
      <div class="row"><span class="ico" style="width:18px;height:18px"></span><div><div class="lbl">Challenge</div><p class="txt">Add a short note on the challenge.</p></div></div>
      <div class="row"><span class="ico" style="width:18px;height:18px;background:var(--grey-light);border-color:var(--grey)"></span><div><div class="lbl">Solution</div><p class="txt">Add a short note on the solution.</p></div></div>
      <div class="row"><span class="ico" style="width:18px;height:18px;background:var(--grey-light);border-color:var(--grey)"></span><div><div class="lbl">Result</div><p class="txt">Add a short note on the result.</p></div></div>
    </div>
    <span class="page">PAGE | 31</span>
  </article>

  <article class="slide">
    <div class="photo" role="img" aria-label="Photo of two hikers celebrating on a summit at sunset" style="left:0;top:0;width:50%;height:100%"></div>
    <div class="brand corner">NORVALE</div>
    <div class="abs" style="left:208px;top:44px;font-size:11px;font-weight:700;color:var(--navy);line-height:1.2">Vision<br>Statement</div>
    <div class="abs" style="left:322px;top:40px;font-size:22px;font-weight:800;color:var(--grey-light);line-height:1">&rdquo;</div>
    <p class="txt abs" style="left:208px;top:82px;width:142px">You can simply impress your audience and add a unique design to your presentation. Easy to change colors, photos and text. A modern layout that is beautifully designed.</p>
    <span class="page">PAGE | 32</span>
  </article>

  <article class="slide">
    <h3 class="s-title">Icons</h3><div class="brand corner">NORVALE</div>
    <svg class="abs" style="left:3%;top:22%;width:94%;height:66%" viewBox="0 0 300 110" aria-label="Icon set">
      <defs>
        <g id="ico-row" fill="none" stroke="#2d4470" stroke-width="1">
          <circle cx="8" cy="8" r="5"/><rect x="21" y="3" width="10" height="10"/><circle cx="44" cy="8" r="5"/><path d="M58 13 L63 3 L68 13 Z"/><rect x="76" y="4" width="12" height="8" rx="1"/><circle cx="100" cy="8" r="5"/><path d="M112 8 h10 M117 3 v10"/><rect x="130" y="3" width="10" height="10" rx="2"/><circle cx="154" cy="8" r="5"/><path d="M166 13 L171 3 L176 13"/><rect x="184" y="3" width="10" height="10"/><circle cx="208" cy="8" r="5"/><path d="M220 10 l4 3 l7 -9"/><rect x="238" y="4" width="12" height="8" rx="1"/><circle cx="262" cy="8" r="5"/><path d="M274 8 h12 M281 3 l5 5 l-5 5"/>
        </g>
      </defs>
      <use href="#ico-row" y="0"/><use href="#ico-row" y="18"/><use href="#ico-row" y="36"/><use href="#ico-row" y="54"/><use href="#ico-row" y="72"/><use href="#ico-row" y="90"/>
    </svg>
    <span class="foot">NORVALE CONSULTING | 2021</span><span class="page">PAGE | 33</span>
  </article>

  <!-- Row 12 -->
  <div></div>
  <article class="slide">
    <div class="abs" style="left:26px;top:26px;font-size:13px;font-weight:800;color:var(--navy)">THANK YOU</div>
    <div class="abs" style="left:26px;top:62px;font-size:5px;font-weight:700;color:var(--ink)">PRESENTER NAME</div>
    <ul class="abs" style="left:26px;top:78px;list-style:none;display:flex;flex-direction:column;gap:4px">
      <li class="row" style="align-items:center;gap:5px"><svg width="9" height="9" viewBox="0 0 10 10"><circle cx="5" cy="5" r="4.5" fill="var(--navy)"/><path d="M5 2.5a1.6 1.6 0 0 1 1.6 1.6C6.6 5.4 5 7.5 5 7.5S3.4 5.4 3.4 4.1A1.6 1.6 0 0 1 5 2.5z" fill="#fff"/></svg><span class="txt">12 Harbor Lane, Suite 4, Lakeview</span></li>
      <li class="row" style="align-items:center;gap:5px"><svg width="9" height="9" viewBox="0 0 10 10"><circle cx="5" cy="5" r="4.5" fill="var(--navy)"/><path d="M3.3 2.8l1 1-.5.7a3.6 3.6 0 0 0 1.7 1.7l.7-.5 1 1-.7.8C4.7 7.2 2.8 5.3 2.5 3.5z" fill="#fff"/></svg><span class="txt">+1 555 010 2040</span></li>
      <li class="row" style="align-items:center;gap:5px"><svg width="9" height="9" viewBox="0 0 10 10"><circle cx="5" cy="5" r="4.5" fill="var(--navy)"/><path d="M3.3 2.8l1 1-.5.7a3.6 3.6 0 0 0 1.7 1.7l.7-.5 1 1-.7.8C4.7 7.2 2.8 5.3 2.5 3.5z" fill="#fff"/></svg><span class="txt">+1 555 010 2041</span></li>
      <li class="row" style="align-items:center;gap:5px"><svg width="9" height="9" viewBox="0 0 10 10"><circle cx="5" cy="5" r="4.5" fill="var(--navy)"/><rect x="2.8" y="3.4" width="4.4" height="3.2" fill="none" stroke="#fff" stroke-width=".7"/><path d="M2.8 3.4 L5 5.2 L7.2 3.4" fill="none" stroke="#fff" stroke-width=".7"/></svg><span class="txt">hello@norvale.example</span></li>
      <li class="row" style="align-items:center;gap:5px"><svg width="9" height="9" viewBox="0 0 10 10"><circle cx="5" cy="5" r="4.5" fill="var(--navy)"/><circle cx="5" cy="5" r="2.2" fill="none" stroke="#fff" stroke-width=".7"/></svg><span class="txt">www.norvale.example</span></li>
    </ul>
    <div class="brand abs" style="left:196px;top:84px;font-size:24px;text-align:center">NORVALE<span class="sub-brand">CONSULTING</span></div>
  </article>
  <div></div>

</main>
</div>
</body>
</html>
```